Faris Methani Business Card

I would like an elegant business card design in both english and arabic.

Ideally a logo design with my name in Arabic (could be a tiger for example)

It should have my Name : Faris Methani
Title: Advisor / Investor
Tel. UAE +971 558 274 903
UK +44 7821 560 287
Email. farmethani412@mailvane.net

I am an active angle investor and have many business interests in the TMT space and invest globally, the design needs to be fresh, elegant and striking.

The design should be catching and grab one's attention when they view the card.

Front card should be in English and Reverse in Arabic....

Target Market(s)

Global Investors, CEO's

Industry/Entity Type

Business

Contact Information for Business Card

Title: Advisor / Investor
Tel. UAE +971 558 274 903
UK +44 7821 560 287

Font styles to use
Serif
Other font styles liked:
• Palantino

Requirements
Must have
• A striking design with a play of my name in Arabic, could be my name that is designed as a tiger for example

```html
<!DOCTYPE html>
<html lang="en">
<head>
<meta charset="utf-8">
<title>Faris Methani Business Card</title>
<link rel="stylesheet" href="https://fonts.googleapis.com/css2?family=Cormorant+SC:wght@500&family=Pathway+Gothic+One&display=swap">
<style>
  :root {
    --page: #ffffff;
    --card: #c8c8ca;
    --ink: #0b0b0c;
    --shadow-grey: #6e686b;
    --lettering: #4f484b;
    --text: #262628;
    --face: #c9c9cb;
    --face-edge: #ffffff;
  }
  * { margin: 0; padding: 0; box-sizing: border-box; }
  html, body {
    width: 1200px; height: 900px; overflow: hidden;
    background: var(--page);
  }
  .canvas { position: relative; width: 1200px; height: 900px; }

  .card { position: absolute; background: var(--card); overflow: hidden; }
  .card--front { left: 0; top: 28px; width: 549px; height: 872px; }
  .card--back { left: 651px; top: 0; width: 549px; height: 872px; }

  .front-name {
    position: absolute;
    left: 118px; top: 400px;
    font-family: "Cormorant SC", "Palatino Linotype", serif;
    font-weight: 500;
    font-size: 104px;
    letter-spacing: -2px;
    white-space: nowrap;
    color: var(--face);
    -webkit-text-stroke: 1.5px var(--face-edge);
    transform-origin: left bottom;
    transform: rotate(-19deg) scaleX(0.52);
    text-shadow:
      -2px -2px 0 var(--ink), -4px -4px 0 var(--ink), -6px -6px 0 var(--ink),
      -8px -8px 0 var(--ink), -10px -10px 0 var(--ink), -12px -12px 0 var(--ink),
      -14px -14px 0 var(--ink), -16px -16px 0 var(--ink), -18px -18px 0 var(--ink),
      -20px -20px 0 var(--ink), -22px -22px 0 var(--ink), -24px -24px 0 var(--ink),
      -26px -26px 0 var(--ink), -28px -28px 0 var(--ink), -30px -30px 0 var(--ink),
      -32px -32px 0 var(--ink), -34px -34px 0 var(--ink), -36px -36px 0 var(--ink),
      -38px -38px 0 var(--ink), -40px -40px 0 var(--ink), -42px -42px 0 var(--ink);
  }

  .back-art { position: absolute; left: 0; top: 0; width: 549px; height: 872px; }
  .diamond { fill: var(--ink); }
  .diamond-shadow { fill: var(--shadow-grey); }

  .contact {
    position: absolute;
    left: 0; width: 549px; top: 524px;
    text-align: center;
    font-family: "Pathway Gothic One", "Arial Narrow", sans-serif;
    font-size: 30px;
    line-height: 58px;
    color: var(--text);
    list-style: none;
  }
  .contact__title { text-transform: uppercase; }
</style>
</head>
<body>
<main class="canvas">
  <section class="card card--front" aria-label="Card front">
    <h1 class="front-name">FARIS METHANI</h1>
  </section>

  <section class="card card--back" aria-label="Card back">
    <svg class="back-art" viewBox="0 0 549 872" xmlns="http://www.w3.org/2000/svg">
      <polygon class="diamond-shadow" points="61,60 94,137 64,218 29,140"/>
      <polygon class="diamond" points="54,58 85,135 56,212 21,138"/>
      <polygon class="diamond-shadow" points="504,60 537,137 507,218 472,140"/>
      <polygon class="diamond" points="497,58 528,135 499,212 464,138"/>
      <g role="img" aria-label="Arabic-style lettering of the name Faris Methani">
        <polygon fill="var(--shadow-grey)" points="122,445 444,318 449,388 126,500"/>
        <polygon fill="var(--lettering)" points="116,440 438,312 443,382 120,494"/>
      </g>
    </svg>
    <ul class="contact">
      <li class="contact__title">Advisor\Investor</li>
      <li>UK:+44 7821 560 287</li>
      <li>UAE:+971 558 274 903</li>
      <li>Email. farmethani412@mailvane.net</li>
    </ul>
  </section>
</main>
</body>
</html>
```